Dorota corporate path of jobs

Looking to make a poster illustration of my wife’s journey in the corporate world over the years since graduating college, showing jobs of the past as well as positions, from past to current illustrating her successes and failures.
Sort of like picture below but with time line on x axis and sucesss on y axis. Would want it to look like a stock chart.
Each company should have a logo of that company on the graph as well as written description of position.
Poster should be 36”x24”
The icon person should be an attractive blond female.
Rough time line:

December 2001: Graduated  Halvern College

January 2002 to June 2002 - First job at Wayfarer Auto Hire Co

June of 2002- February 2007: Velt Power

April 2007-March 2011: Tamsin Reyk

March 2011 - June 2012 : Halford Quine

November 2012: R.T. Velloway Vice President

April 2018: Executive Director R.T. Velloway

April 2023: Managing Director at R.T. Velloway Unsuccessful

April 2024 Dorota Made Managing Director @ R.T. Velloway

Requirements
Nice to have
• Stock chart graph with NYC background showing the ups and downs of the path.

```html
<!DOCTYPE html>
<html lang="en">
<head>
<meta charset="utf-8">
<title>Dorota Corporate Path</title>
<link rel="stylesheet" href="https://fonts.googleapis.com/css2?family=Arvo:wght@700&family=Oswald:wght@500&family=Rokkitt:wght@400;500&display=swap">
<style>
  :root {
    --ink: #000000;
    --paper: #ffffff;
    --gold: #f0b400;
    --gold-line: #7a6530;
    --base: #1c7ea6;
    --yellow: #f2a600;
    --yellow-side: #d98800;
    --yellow-top: #ffc21a;
    --green: #8f9a00;
    --green-side: #667000;
    --green-top: #b3bf00;
    --red: #d41f22;
    --red-side: #9e1214;
    --red-top: #f0373a;
    --orange: #f08400;
    --orange-side: #c26200;
    --orange-top: #ff9a1f;
    --tx-yellow: #f2a600;
    --tx-green: #a3ad00;
    --tx-red: #e8262a;
    --tx-orange: #f28a00;
  }
  * { margin: 0; padding: 0; box-sizing: border-box; }
  html, body { width: 1200px; height: 800px; overflow: hidden; background: var(--ink); }
  .poster { position: relative; width: 1200px; height: 800px; background: var(--ink); overflow: hidden; }
  .skyline { position: absolute; left: 36px; top: 0; width: 1160px; height: 570px;
    background: linear-gradient(180deg, #0b0b0b 0%, #161410 60%, #0a0a0a 100%); }
  .heroine { position: absolute; left: 78px; top: 58px; width: 222px; height: 440px; border-radius: 100px 100px 40px 40px;
    background: linear-gradient(180deg, #b8432e 0%, #f1d5bd 30%, #6a2a8a 55%, #e8a27e 80%, #5a1f6e 100%); opacity: .85; }
  .chart { position: absolute; left: 0; top: 0; }
  .title { position: absolute; top: 28px; left: 0; width: 1200px; text-align: center;
    font-family: "Arvo", serif; font-weight: 700; font-size: 38px; letter-spacing: 4px; color: var(--paper); }
  .dates { position: absolute; top: 586px; width: 120px; text-align: center;
    font-family: "Oswald", sans-serif; font-weight: 500; font-size: 18px; line-height: 20px; color: var(--paper); letter-spacing: .5px; }
  .dates.single { top: 596px; }
  .brand { position: absolute; top: 641px; width: 90px; height: 45px; background: var(--paper); border-radius: 4px;
    display: flex; align-items: center; justify-content: center; text-align: center;
    font-family: "Rokkitt", serif; font-weight: 500; font-size: 13px; line-height: 13px; color: #1b1b1b; padding: 0 4px; }
  .caption { position: absolute; top: 705px; width: 130px; text-align: center;
    font-family: "Rokkitt", serif; font-weight: 400; font-size: 16px; line-height: 17px; }
  .c-yellow { color: var(--tx-yellow); }
  .c-green { color: var(--tx-green); }
  .c-red { color: var(--tx-red); }
  .c-orange { color: var(--tx-orange); }
  .front-yellow { fill: var(--yellow); } .side-yellow { fill: var(--yellow-side); } .top-yellow { fill: var(--yellow-top); }
  .front-green { fill: var(--green); } .side-green { fill: var(--green-side); } .top-green { fill: var(--green-top); }
  .front-red { fill: var(--red); } .side-red { fill: var(--red-side); } .top-red { fill: var(--red-top); }
  .front-orange { fill: var(--orange); } .side-orange { fill: var(--orange-side); } .top-orange { fill: var(--orange-top); }
  .base { fill: none; stroke: var(--base); stroke-width: 4; stroke-linecap: round; }
  .horizon { stroke: var(--gold-line); stroke-width: 1; }
  .timeline { stroke: var(--paper); stroke-width: 1; }
  .dot { fill: var(--gold); }
  .dash { stroke-width: 3; stroke-linecap: round; }
  .icon { fill: none; stroke: #1a1a1a; stroke-width: 2; stroke-linejoin: round; stroke-linecap: round; }
  .award { fill: #111; }
</style>
</head>
<body>
<main class="poster">
  <div class="skyline" role="img" aria-label="Night skyline of Manhattan towers outlined in gold"></div>

  <svg class="chart" width="1200" height="800" viewBox="0 0 1200 800" aria-hidden="true">
    <defs>
      <symbol id="thumb" viewBox="0 0 40 40">
        <g class="icon">
          <rect x="4" y="20" width="7" height="15"/>
          <path d="M11 21 L16 21 L21 9 C24 8 26 11 25 15 L24 19 L33 19 C35 19 36 21 35 23 L33 33 C32 35 31 35 29 35 L11 35 Z"/>
          <path d="M20 1 L20 4 M12 3 L14 6 M28 3 L26 6 M6 9 L9 11 M34 9 L31 11"/>
        </g>
      </symbol>
    </defs>

    <line class="horizon" x1="0" y1="424" x2="1200" y2="424"/>

    <g class="dashes">
      <line class="dash" x1="363" y1="93" x2="407" y2="93" style="stroke:var(--gold)"/>
      <line class="dash" x1="417" y1="93" x2="461" y2="93" style="stroke:var(--green)"/>
      <line class="dash" x1="471" y1="93" x2="515" y2="93" style="stroke:var(--red)"/>
      <line class="dash" x1="525" y1="93" x2="569" y2="93" style="stroke:var(--orange)"/>
      <line class="dash" x1="579" y1="93" x2="623" y2="93" style="stroke:var(--orange)"/>
      <line class="dash" x1="633" y1="93" x2="677" y2="93" style="stroke:var(--green)"/>
      <line class="dash" x1="687" y1="93" x2="731" y2="93" style="stroke:var(--red)"/>
      <line class="dash" x1="741" y1="93" x2="785" y2="93" style="stroke:var(--gold)"/>
      <line class="dash" x1="795" y1="93" x2="839" y2="93" style="stroke:var(--orange)"/>
    </g>

    <!-- bars: front x = centre-33, width 50, depth 15 -->
    <g class="bar">
      <path class="base" d="M81 568 L143 568 L157 556"/>
      <rect class="front-yellow" x="87" y="494" width="50" height="72"/>
      <polygon class="side-yellow" points="137,494 152,484 152,556 137,566"/>
      <polygon class="top-yellow" points="87,494 102,484 152,484 137,494"/>
      <use href="#thumb" x="98" y="505" width="34" height="34"/>
    </g>
    <g class="bar">
      <path class="base" d="M203 568 L265 568 L279 556"/>
      <rect class="front-green" x="209" y="449" width="50" height="117"/>
      <polygon class="side-green" points="259,449 274,439 274,556 259,566"/>
      <polygon class="top-green" points="209,449 224,439 274,439 259,449"/>
      <use href="#thumb" x="220" y="482" width="34" height="34"/>
    </g>
    <g class="bar">
      <path class="base" d="M325 568 L387 568 L401 556"/>
      <rect class="front-red" x="331" y="380" width="50" height="186"/>
      <polygon class="side-red" points="381,380 396,370 396,556 381,566"/>
      <polygon class="top-red" points="331,380 346,370 396,370 381,380"/>
      <use href="#thumb" x="342" y="448" width="34" height="34"/>
    </g>
    <g class="bar">
      <path class="base" d="M447 568 L509 568 L523 556"/>
      <rect class="front-yellow" x="453" y="319" width="50" height="247"/>
      <polygon class="side-yellow" points="503,319 518,309 518,556 503,566"/>
      <polygon class="top-yellow" points="453,319 468,309 518,309 503,319"/>
      <use href="#thumb" x="464" y="418" width="34" height="34"/>
    </g>
    <g class="bar">
      <path class="base" d="M569 568 L631 568 L645 556"/>
      <rect class="front-orange" x="575" y="227" width="50" height="339"/>
      <polygon class="side-orange" points="625,227 640,217 640,556 625,566"/>
      <polygon class="top-orange" points="575,227 590,217 640,217 625,227"/>
      <use href="#thumb" x="586" y="370" width="34" height="34"/>
    </g>
    <g class="bar">
      <path class="base" d="M691 568 L753 568 L767 556"/>
      <rect class="front-green" x="697" y="174" width="50" height="392"/>
      <polygon class="side-green" points="747,174 762,164 762,556 747,566"/>
      <polygon class="top-green" points="697,174 712,164 762,164 747,174"/>
      <use href="#thumb" x="708" y="345" width="34" height="34"/>
    </g>
    <g class="bar">
      <path class="base" d="M813 568 L875 568 L889 556"/>
      <rect class="front-red" x="819" y="138" width="50" height="428"/>
      <polygon class="side-red" points="869,138 884,128 884,556 869,566"/>
      <polygon class="top-red" points="819,138 834,128 884,128 869,138"/>
      <use href="#thumb" x="830" y="326" width="34" height="34"/>
    </g>
    <g class="bar">
      <path class="base" d="M935 568 L997 568 L1011 556"/>
      <rect class="front-yellow" x="941" y="96" width="50" height="470"/>
      <polygon class="side-yellow" points="991,96 1006,86 1006,556 991,566"/>
      <polygon class="top-yellow" points="941,96 956,86 1006,86 991,96"/>
      <use href="#thumb" x="952" y="303" width="34" height="34" transform="rotate(180 969 320)"/>
    </g>
    <g class="bar">
      <path class="base" d="M1057 568 L1119 568 L1133 556"/>
      <rect class="front-orange" x="1063" y="58" width="50" height="508"/>
      <polygon class="side-orange" points="1113,58 1128,48 1128,556 1113,566"/>
      <polygon class="top-orange" points="1063,58 1078,48 1128,48 1113,58"/>
      <g class="award">
        <polygon points="1093,249 1096,258 1105,258 1098,263 1101,272 1093,266 1085,272 1088,263 1081,258 1090,258"/>
        <polygon points="1093,272 1112,292 1096,348 1090,348 1074,292"/>
        <polygon points="1080,348 1106,348 1118,360 1093,368 1068,360"/>
      </g>
    </g>

    <line class="timeline" x1="0" y1="663" x2="1200" y2="663"/>
    <circle class="dot" cx="181" cy="663" r="3.5"/>
    <circle class="dot" cx="303" cy="663" r="3.5"/>
    <circle class="dot" cx="425" cy="663" r="3.5"/>
    <circle class="dot" cx="547" cy="663" r="3.5"/>
    <circle class="dot" cx="669" cy="663" r="3.5"/>
    <circle class="dot" cx="791" cy="663" r="3.5"/>
    <circle class="dot" cx="913" cy="663" r="3.5"/>
    <circle class="dot" cx="1035" cy="663" r="3.5"/>
  </svg>

  <div class="heroine" role="img" aria-label="Illustrated businesswoman in a cream jacket and purple skirt stepping up onto the first bar"></div>

  <h1 class="title">Dorota Corporate Path</h1>

  <div class="dates single" style="left:58px">Dec - 2001</div>
  <div class="dates" style="left:180px">Jan 2002<br>Jun 2002</div>
  <div class="dates" style="left:302px">Jun 2002<br>Feb 2007</div>
  <div class="dates" style="left:424px">Apr 2007<br>Mar 2011</div>
  <div class="dates" style="left:546px">Mar 2011<br>Jun 2012</div>
  <div class="dates" style="left:668px">Jun 2012<br>Nov 2012</div>
  <div class="dates" style="left:790px">Nov 2012<br>Apr 2018</div>
  <div class="dates" style="left:912px">Apr 2018<br>Apr 2023</div>
  <div class="dates" style="left:1034px">Apr 2023<br>Apr 2024</div>

  <div class="brand" style="left:73px">Halvern College</div>
  <div class="brand" style="left:199px">Wayfarer Auto Hire Co</div>
  <div class="brand" style="left:319px">Velt Power</div>
  <div class="brand" style="left:440px">Tamsin Reyk</div>
  <div class="brand" style="left:560px">Halford Quine</div>
  <div class="brand" style="left:683px">R.T. Velloway</div>
  <div class="brand" style="left:806px">R.T. Velloway</div>
  <div class="brand" style="left:927px">R.T. Velloway</div>
  <div class="brand" style="left:1047px">R.T. Velloway</div>

  <p class="caption c-yellow" style="left:53px">Graduated<br>Halvern College</p>
  <p class="caption c-green" style="left:179px">First job at<br>Wayfarer Auto<br>Hire Co</p>
  <p class="caption c-red" style="left:299px">Velt<br>Power</p>
  <p class="caption c-yellow" style="left:420px">Tamsin<br>Reyk</p>
  <p class="caption c-orange" style="left:540px">Halford<br>Quine</p>
  <p class="caption c-green" style="left:663px">R.T. Velloway<br>Vice President</p>
  <p class="caption c-red" style="left:786px">Executive<br>Director<br>R.T. Velloway</p>
  <p class="caption c-yellow" style="left:907px">Managing<br>Director at<br>R.T. Velloway<br>Unsuccessful</p>
  <p class="caption c-orange" style="left:1027px">Dorota Made<br>Managing<br>Director at<br>R.T. Velloway</p>
</main>
</body>
</html>
```